RV7 church inspiring foldout brochure/booklet

RV7, a non-denominational christian church needs a full color, creative foldout brochure that provides next steps for guests who come to know Jesus. We want to provide basic information in a creative way as the first step in the follow-up process. We are in the midst of re-branding and would like the brochure to reflect relationship and the power we have when in relationship to affect change, etc.; making a positive impact on each other, the community and the world. We want the design to be minimalist and friendly. We do Not want something that looks churchy or cliche Christian. The final design should communicate community. Our new church website is under construction, the old website may be helpful to express our vision and values but should not be looked to for design inspiration (www.rv7.example).
We're basing our outline and content off of Lanternway.example's "Begin the walk" manual (attached below). Our tagline is "The Strength of a Woven Path."
Updates

Thank you all for your patience as I navigate this new process. I have updated the brief. Please let me know if there is anything further that would be helpful.

Reason: We would like to expand the pool of designers.

Reason: We have a couple of designs that we are looking at more closely and sending out for feedback.

Target Market(s)

Adults in the North Eastern United States aged 18-50. Persons with limited church or faith background. We're located in the historic business district of Bethlehem, PA, USA- between Philadelphia and New York City. We have an average age of 33 with the majority of our demographic base under the age of 30 (families and children). However, we frequently have guests come in from the surrounding neighborhood and shopping district.

Industry/Entity Type

Church

Colors
85abd2
0355a3
3176b5
faf289
fece3e
00a88f
33b7a4
a64599
9bcb3c

Requirements
Must have
• Our tagline should be featured somewhere in the brochure: "The strength of a woven path." The emphasis is the on the power inherent in connecting/relationships/community.

We use Mac and Windows platforms running Microsoft Office Suite of Programs, as well as Pages et al. At this point in our design journey we need the ability to edit content. Content should be treated like place holders.
Nice to have
• Brochure could be square or a shape other than rectangular. Would appreciate the layout being other than tri-fold rectangular.

Colors below are merely suggestions based on some current building design schemes.
Should not have
• Should not use old-style, serif fonts like Times New Roman. Should not include cliche "Christian" iconography or imagery. We're not a typically "churchy" church.

```html
<!DOCTYPE html>
<html lang="en">
<head>
<meta charset="utf-8">
<title>RV7 – Saved! Now What? Booklet</title>
<link rel="stylesheet" href="https://fonts.googleapis.com/css2?family=Arimo:wght@400&family=Roboto+Slab:wght@300&family=Bitter:wght@700&family=Archivo+Black&family=PT+Sans:ital,wght@0,400;0,700;1,400;1,700&family=Open+Sans:wght@700;800&family=Michroma&display=swap">
<style>
:root{
  --ink:#111;
  --purple:#a64599;
  --blue:#1f78c1;
  --teal:#33b7a4;
  --quote:#3a9fc9;
  --lime:#9bcb3c;
  --parch-light:#f7f0c9;
  --parch:#ece0a6;
  --parch-dark:#d9c887;
  --page:#fff;
}
*{margin:0;padding:0;box-sizing:border-box}
html,body{width:1200px;height:1186px;overflow:hidden;background:var(--page)}
body{position:relative;font-family:"PT Sans",sans-serif;color:var(--ink)}

.sheet-label{position:absolute;font-family:"Michroma",sans-serif;font-size:22px;letter-spacing:2px;background:var(--page);padding:0 10px}
.bracket{position:absolute;border:2px solid var(--ink)}
.bracket--top{border-bottom:none;height:24px}
.bracket--bottom{border-top:none;height:24px}

.panel{position:absolute;width:505px;height:505px;overflow:hidden}
.parchment{background:
  radial-gradient(ellipse at 30% 40%,var(--parch-light) 0%,transparent 60%),
  radial-gradient(ellipse at 80% 80%,var(--parch-light) 0%,transparent 55%),
  linear-gradient(135deg,var(--parch) 0%,var(--parch-dark) 100%)}

.brand{position:absolute;display:flex;align-items:center;gap:8px;font-family:"Open Sans",sans-serif;font-weight:800;color:var(--ink)}
.brand__dot{width:14px;height:14px;border-radius:50%;background:var(--teal)}

/* front */
.front{left:14px;top:64px}
.front__art{position:absolute;left:0;top:0;width:505px;height:255px;
  background:radial-gradient(circle at 28% 78%,#ffe08a 0%,#f2a33a 14%,#7a3b10 38%,#1a0d05 70%,#000 100%)}
.front__band{position:absolute;left:0;top:255px;width:505px;height:59px;background:var(--lime);
  border-top:3px solid #c8e48d;border-bottom:3px solid #c8e48d}
.front__tagline{position:absolute;left:24px;top:263px;font-family:"Roboto Slab",sans-serif;font-weight:300;font-size:31px;color:var(--purple)}
.front__title{position:absolute;left:38px;top:335px;font-family:"Arimo",sans-serif;font-size:82px;line-height:1;color:var(--ink)}
.front__sub{position:absolute;left:40px;top:418px;font-family:"Arimo",sans-serif;font-size:44px;line-height:1;color:var(--blue)}
.front .brand{left:385px;top:380px;font-size:28px}

/* back */
.back{left:551px;top:64px}
.back__art{position:absolute;left:0;top:0;width:505px;height:402px;
  background:radial-gradient(ellipse at 50% 55%,#c9b9a0 0%,#8aa67a 40%,#4f8a6e 70%,#2f5b4c 100%)}
.back__circle{position:absolute;left:123px;top:123px;width:258px;height:258px;border-radius:50%;background:#fff;
  display:flex;flex-direction:column;justify-content:center;align-items:center;gap:6px;
  font-family:"Bitter",serif;font-weight:700;font-size:19px;text-align:center;box-shadow:0 0 14px rgba(255,255,255,.8)}
.back__foot{position:absolute;left:0;top:402px;width:505px;height:103px}
.back__stay{position:absolute;left:34px;top:436px;font-family:"Archivo Black",sans-serif;font-size:31px;letter-spacing:.5px}
.back .brand{left:400px;top:440px;font-size:26px}

.dimension{position:absolute;left:1078px;top:64px;width:2px;height:505px;background:var(--ink)}
.dimension::before,.dimension::after{content:"";position:absolute;left:-6px;border:7px solid transparent}
.dimension::before{top:-8px;border-bottom:9px solid var(--ink);border-top:none}
.dimension::after{bottom:-8px;border-top:9px solid var(--ink);border-bottom:none}
.dimension__label{position:absolute;left:1012px;top:575px;font-family:"Michroma",sans-serif;font-size:15px}

.fold{position:absolute;left:1086px;top:633px}
.fold__text{position:absolute;left:8px;top:32px;width:80px;text-align:center;font-family:"PT Sans",sans-serif;font-size:18px;line-height:1.1}
.fold__w{position:absolute;left:28px;top:-6px;font-size:10px}
.fold__h{position:absolute;left:-18px;top:48px;font-size:10px;transform:rotate(-90deg)}

/* inside left */
.inside-left{left:14px;top:594px;padding:38px 28px 0 28px;font-size:14.5px;line-height:1.3}
.welcome{font-family:"Open Sans",sans-serif;font-weight:800;font-size:22px;color:var(--purple);text-align:center;margin-bottom:10px}
.inside-left p{margin-bottom:12px}
.inside-left .indent{padding-left:22px;padding-right:20px}
.lead{color:var(--purple);font-weight:700}
.point{font-family:"Open Sans",sans-serif;font-weight:700;font-size:11.5px;line-height:1.4}
.scripture{color:var(--quote);font-style:italic;padding-left:22px;padding-right:20px}
.scripture cite{color:var(--ink);font-style:normal}
.inside-left .brand{left:432px;top:458px;font-size:18px}

/* inside right */
.inside-right{left:551px;top:594px}
.intro{position:absolute;left:18px;top:26px;width:128px;font-style:italic;font-weight:700;font-size:13.5px;line-height:18px}
.intro em{color:var(--quote)}
.step{position:absolute;left:153px;width:334px}
.step--wide{left:18px;width:470px}
.step h2{font-family:"Open Sans",sans-serif;font-weight:700;font-size:11px;line-height:14px;color:var(--purple);margin-bottom:3px}
.step p{font-size:9px;line-height:11.5px}
.step--read{top:24px}
.step--pray{top:104px}
.step--church{top:180px}
.step--living{top:258px}
.step--share{top:330px}
.step--sidetrack{top:404px}
</style>
</head>
<body>

<div class="bracket bracket--top" style="left:106px;top:32px;width:310px"></div>
<span class="sheet-label" style="left:206px;top:18px">FRONT</span>
<div class="bracket bracket--top" style="left:648px;top:32px;width:312px"></div>
<span class="sheet-label" style="left:714px;top:18px">BACK</span>

<section class="panel front parchment">
  <div class="front__art" role="img" aria-label="Hands reaching toward a glowing warm light on a dark background"></div>
  <div class="front__band"></div>
  <p class="front__tagline">The strength of a woven path</p>
  <h1 class="front__title">SAVED!</h1>
  <p class="front__sub">NOW WHAT?</p>
  <div class="brand"><span class="brand__dot"></span>RV7</div>
</section>

<section class="panel back">
  <div class="back__art" role="img" aria-label="Cupped hands holding a glowing circle amid soft green clouds"></div>
  <div class="back__circle">
    <span>Connect with God</span>
    <span>Connect with his Word</span>
    <span>Connect with Community</span>
    <span>Connect with Life</span>
  </div>
  <div class="back__foot parchment"></div>
  <p class="back__stay">STAY CONNECTED</p>
  <div class="brand"><span class="brand__dot"></span>RV7</div>
</section>

<div class="dimension"></div>
<span class="dimension__label">210MM</span>

<div class="fold">
  <svg width="92" height="95" viewBox="0 0 92 95">
    <polygon points="2,12 88,12 88,93 2,93" fill="#fff" stroke="#555"/>
    <polyline points="2,12 12,4 92,4 88,12" fill="#eee" stroke="#555"/>
  </svg>
  <span class="fold__w">210mm</span>
  <span class="fold__h">210mm</span>
  <span class="fold__text">210mm Square</span>
</div>

<section class="panel inside-left parchment">
  <h2 class="welcome">WELCOME TO GOD'S FAMILY!</h2>
  <p>You have made the <strong>most important decision of your life</strong>, choosing to follow Jesus. As a new believer, you have questions. You prayed and asked Jesus into your heart, but now you want to know what that actually means.</p>
  <p class="point indent"><span class="lead">First,</span> you need to know that means you are headed in the right direction - you are bound for heaven. Before coming to Christ, you were separated from God by sin and on your way to a very real place called hell! But Jesus has saved you by dying on the cross in your place.</p>
  <p class="indent" style="margin-bottom:2px">The Bible says:</p>
  <p class="scripture">Since we have been made right in God's sight by the blood of Christ, he will certainly save us from God's judgment. For since we were restored to friendship with God by the death of his Son while we were still his enemies, we will certainly be delivered from eternal punishment by his life. <cite>(Romans 5:9–10)</cite></p>
  <p class="point indent"><span class="lead">Second,</span> you need to know that you have been given a new life!</p>
  <p class="indent" style="margin-bottom:2px">The Bible says:</p>
  <p class="scripture">"Those who become Christians become new persons. They are not the same anymore, for the old life is gone. A new life has begun!" <cite>(2 Corinthians 5:17)</cite></p>
  <div class="brand"><span class="brand__dot"></span>RV7</div>
</section>

<section class="panel inside-right parchment">
  <p class="intro">As a new believer, you can expect to have new attitudes and desires. You may need to replace some old habits and patterns with new activities that will help you to grow your new life in Christ. Growth takes time, but it begins - <em>right now</em> - where you are. Here is what you need to know in order to get off on the right foot:</p>
  <div class="step step--read"><h2>READ THE BIBLE</h2><p>The Bible will tell you everything you need to know in order to grow in your spiritual life. Because God speaks through His Word, you will get to know Him better and learn what pleases Him. As you obey His Word, you will grow strong and begin to see positive changes in your life.</p></div>
  <div class="step step--pray"><h2>PRAY</h2><p>Prayer is one of the greatest privileges we have as a child of God. Just think, the God of all creation wants to hear from you! You can call on the Lord any hour of the day or night and He will listen. It doesn't matter to God if your prayers are eloquent or flowery - it matters only that you pray with a pure and sincere heart.</p></div>
  <div class="step step--church"><h2>FIND A CHURCH TO ATTEND</h2><p>Church plays a vital role in your spiritual growth. Fellowship with other Christians will keep you spiritually active and give you much needed encouragement and support. Church provides you with instruction from God's Word and gives you the training and opportunity to use your God-given gifts and abilities.</p></div>
  <div class="step step--living"><h2>START LIVING FOR GOD</h2><p>A sure sign of a changed heart is the desire to live for God. What does this mean? It means that you want to please God and to obey Him as best you know how. You will begin to filter your thoughts and actions through God's Word in order to become a reflection of Jesus Christ.</p></div>
  <div class="step step--wide step--share"><h2>SHARE YOUR FAITH</h2><p>Good news is hard to keep to yourself! God wants you to share your newfound faith with others. You don't have to wait until you're an expert in the Bible to witness to others. You can share what you know - your own story of what Jesus has done for you. <strong>Visit www.lanternwayresources.example</strong> to obtain a useful tool for learning to share your faith entitled The Short Story Guide.</p></div>
  <div class="step step--wide step--sidetrack"><h2>DON'T GET SIDETRACKED</h2><p>Being a Christian is not always easy. There will be times when you'll feel pressured to back down or give in. When you became a child of God, you also became an enemy of the devil; and he will try to tempt you into disobeying God. It isn't a sin to be tempted - even Jesus experienced temptation <strong>(see Luke 4:1–3)</strong> - but giving in to the temptation is sin. Christians will experience times of testing and trials, but God promises to be with us and give us the strength we need to get through hard times.</p></div>
</section>

<div class="bracket bracket--bottom" style="left:106px;top:1112px;width:950px"></div>
<span class="sheet-label" style="left:396px;top:1120px">INSIDES PAGES</span>

</body>
</html>
```